Business Cards used to invite people to our church

We are a church and have need of a business card sized advertisement that allows our members to hand them out in order to invite people to the church. I need the front of the card to say "You're Invited" or "Come Check us out". with the service times on the back of the card later.
I have attached one of the OLD cards we have used in the past, but we want a complete makeover, into a more modern style that does not require the image.
I am also replacing the old logo with a newer "flat" logo which is attached.
Please use marketing colors. (blue or red or something that catches attention)
Create a card that DOES NOT have the picture of the two people on the front
The information on the sample card back is correct to go onto new card
Target Market(s)
anyone
Industry/Entity Type
Business
Contact Information for Business Card
sertice times and address information which you can get from the sample card I uploaded. It should have "You're Invited" or "Come Check us out" on the front of the card with out logo.

```html
<!DOCTYPE html>
<html lang="en">
<head>
<meta charset="utf-8">
<title>Grace Harbor Fellowship – Service Times Card</title>
<link rel="stylesheet" href="https://fonts.googleapis.com/css2?family=Overpass:wght@300;400;700&family=Roboto+Condensed:wght@700&display=swap">
<style>
  :root {
    --page-bg: #ffffff;
    --card-blue: #273273;
    --card-blue-light: #34408a;
    --card-blue-deep: #222c68;
    --ink: #ffffff;
  }
  html, body {
    margin: 0;
    padding: 0;
    width: 1200px;
    height: 1000px;
    overflow: hidden;
    background: var(--page-bg);
  }
  .canvas {
    position: relative;
    width: 1200px;
    height: 1000px;
  }
  .card {
    position: absolute;
    left: 70px;
    top: 168px;
    width: 1056px;
    height: 616px;
    background: var(--card-blue);
    overflow: hidden;
    color: var(--ink);
    font-family: "Overpass", "Helvetica Neue", Arial, sans-serif;
  }
  .card__photo {
    position: absolute;
    inset: 0;
    background:
      radial-gradient(ellipse 45% 55% at 50% 45%, var(--card-blue-light) 0%, rgba(52,64,138,0) 100%),
      linear-gradient(180deg, var(--card-blue) 0%, var(--card-blue-deep) 100%);
  }
  .contact {
    position: absolute;
    left: 0;
    right: 0;
    top: 62px;
    text-align: center;
  }
  .contact__name {
    margin: 0;
    font-weight: 700;
    font-size: 36px;
    line-height: 44px;
  }
  .contact__line {
    margin: 0;
    font-weight: 300;
    font-size: 33px;
    line-height: 44px;
  }
  .schedule {
    position: absolute;
    left: 207px;
    top: 240px;
    width: 700px;
  }
  .schedule__row {
    position: absolute;
    left: 0;
    width: 700px;
    height: 90px;
  }
  .schedule__label {
    position: absolute;
    left: 0;
    top: 14px;
    font-size: 28px;
    font-weight: 400;
    line-height: 34px;
  }
  .schedule__label sup {
    font-size: 15px;
    vertical-align: 12px;
    line-height: 0;
  }
  .schedule__rule {
    position: absolute;
    left: 0;
    top: 68px;
    width: 485px;
    height: 2px;
    background: var(--ink);
  }
  .schedule__clock {
    position: absolute;
    left: 524px;
    top: 0;
    width: 76px;
    height: 76px;
  }
  .schedule__time {
    position: absolute;
    left: 571px;
    top: 46px;
    font-family: "Roboto Condensed", "Arial Narrow", sans-serif;
    font-weight: 700;
    font-size: 27px;
    letter-spacing: -0.5px;
    line-height: 32px;
  }
</style>
</head>
<body>
<div class="canvas">
  <section class="card">
    <div class="card__photo" role="img" aria-label="Soft blue-toned photo of a worship congregation with hands raised"></div>

    <header class="contact">
      <h1 class="contact__name">Grace Harbor Fellowship</h1>
      <p class="contact__line">2418 W. Cedar Lane – Millbrook, TX 75099</p>
      <p class="contact__line">1–800–555–0192</p>
    </header>

    <div class="schedule">
      <div class="schedule__row" style="top:0">
        <span class="schedule__label">1<sup>st</sup> Service</span>
        <span class="schedule__rule"></span>
        <svg class="schedule__clock" viewBox="0 0 76 76" aria-hidden="true">
          <path d="M72 38 A34 34 0 1 0 38 72" fill="none" stroke="#fff" stroke-width="7" stroke-linecap="round"/>
          <path d="M38 20 V38 H24" fill="none" stroke="#fff" stroke-width="6" stroke-linecap="round" stroke-linejoin="round"/>
        </svg>
        <span class="schedule__time">9:00am</span>
      </div>

      <div class="schedule__row" style="top:115px">
        <span class="schedule__label">2<sup>nd</sup> Service</span>
        <span class="schedule__rule" style="top:72px"></span>
        <svg class="schedule__clock" viewBox="0 0 76 76" aria-hidden="true">
          <path d="M72 38 A34 34 0 1 0 38 72" fill="none" stroke="#fff" stroke-width="7" stroke-linecap="round"/>
          <path d="M38 20 V38 L25 30" fill="none" stroke="#fff" stroke-width="6" stroke-linecap="round" stroke-linejoin="round"/>
        </svg>
        <span class="schedule__time">11:00am</span>
      </div>

      <div class="schedule__row" style="top:230px">
        <span class="schedule__label">Wed. Bible class</span>
        <span class="schedule__rule" style="top:76px"></span>
        <svg class="schedule__clock" viewBox="0 0 76 76" aria-hidden="true" style="left:526px">
          <path d="M72 38 A34 34 0 1 0 38 72" fill="none" stroke="#fff" stroke-width="7" stroke-linecap="round"/>
          <path d="M38 19 V38 L27 50" fill="none" stroke="#fff" stroke-width="6" stroke-linecap="round" stroke-linejoin="round"/>
        </svg>
        <span class="schedule__time" style="top:48px">7:00pm</span>
      </div>
    </div>
  </section>
</div>
</body>
</html>
```